ambitious event and festival agency from austria needs fresh business card design

A new design is due for the new headquarters and the new challenges. We organize events for different target groups from 16 to 60 years. The design should therefore be straightforward and not confused, so we are open to new colors and the logo may also be changed. In general, however, the most interesting suggestions are the most interesting ones. after this order we are looking for more graphics for partyvelt facebook instagramm homepage etc A new design is due for the new headquarters and the new challenges. We organize events for different target groups from 16 to 60 years. The design should therefore be straightforward and not confused, so we are open to new colors and the logo may also be changed. In general, however, the most interesting suggestions are the most interesting ones. after this order we are looking for more graphics for partyvelt facebook instagramm homepage etc A new design is due for the new headquarters and the new challenges. We organize events for different target groups from 16 to 60 years. The design should therefore be straightforward and not confused, so we are open to new colors and the logo may also be changed. In general, however, the most interesting suggestions are the most interesting ones. after this order we are looking for more graphics for partyvelt facebook instagramm homepage etc

Reason: I am sorry for this decision but i need some more time. No new designs please, there are so many good ones and I will have made a decision in the next 3 days.

Target Market(s)

Industry/Entity Type

Business

Font styles to use
Serif
Sans Serif

Colors

Designer to choose colors to be used in the design.

Requirements
Must have
Nice to have
Should not have

```html
<!DOCTYPE html>
<html lang="en">
<head>
<meta charset="utf-8">
<title>partyvelt business card</title>
<link rel="stylesheet" href="https://fonts.googleapis.com/css2?family=Roboto:wght@400;500;700&family=Roboto+Condensed:wght@500&display=swap">
<style>
  :root {
    --backdrop: #e4e4e4;
    --card-white: #f7f7f7;
    --brand-red: #b12634;
    --ink-grey: #5b6166;
    --text-grey: #4a4d50;
    --white: #ffffff;
  }
  * { margin: 0; padding: 0; box-sizing: border-box; }
  html, body {
    width: 1200px; height: 960px; overflow: hidden;
    background: var(--backdrop);
    font-family: "Roboto", sans-serif;
  }
  .card {
    position: absolute; left: 312px; width: 600px; height: 342px;
  }
  .card--front { top: 113px; background: var(--card-white); }
  .card--back { top: 472px; background: var(--brand-red); }

  .wordmark {
    position: absolute; display: flex; align-items: center; gap: 8px;
    font-family: "Roboto", sans-serif; font-weight: 500; line-height: 1;
  }
  .wordmark__square { width: 12px; height: 12px; background: var(--brand-red); }
  .card--front .wordmark { left: 53px; top: 66px; font-size: 46px; color: var(--ink-grey); }

  .contact { position: absolute; left: 53px; top: 188px; font-size: 14px; color: var(--text-grey); }
  .contact__company { font-weight: 700; line-height: 18px; }
  .contact__address { line-height: 18px; margin-bottom: 12px; }
  .contact__line { display: flex; align-items: center; gap: 9px; line-height: 19.5px; }
  .contact__icon { width: 12px; height: 12px; fill: var(--brand-red); }

  .person { position: absolute; right: 50px; top: 219px; text-align: right; }
  .person__name {
    font-family: "Roboto Condensed", sans-serif; font-weight: 500;
    font-size: 22px; color: var(--brand-red); line-height: 26px;
  }
  .person__role { font-size: 15px; font-weight: 500; color: var(--ink-grey); line-height: 20px; }
  .edge-tab { position: absolute; right: 0; top: 221px; width: 13px; height: 41px; background: var(--brand-red); }

  .card--back .wordmark { right: 44px; top: 240px; font-size: 42px; color: var(--white); }
  .card--back .wordmark__square { background: var(--white); }
  .back__url {
    position: absolute; right: 42px; top: 288px;
    font-size: 13px; letter-spacing: 0.48em; color: var(--white);
  }
</style>
</head>
<body>
  <section class="card card--front">
    <div class="wordmark"><span class="wordmark__square"></span><span>partyvelt</span></div>

    <div class="contact">
      <p class="contact__company">partyvelt</p>
      <p class="contact__address">Lindenweg 12, A4600 wels</p>
      <p class="contact__line">
        <svg class="contact__icon" viewBox="0 0 24 24" aria-hidden="true"><path d="M6.6 10.8a15.1 15.1 0 0 0 6.6 6.6l2.2-2.2a1 1 0 0 1 1-.25 11.4 11.4 0 0 0 3.6.57 1 1 0 0 1 1 1V20a1 1 0 0 1-1 1A17 17 0 0 1 3 4a1 1 0 0 1 1-1h3.5a1 1 0 0 1 1 1c0 1.25.2 2.45.57 3.57a1 1 0 0 1-.25 1z"/></svg>
        <span>+43 660 418 273 5</span>
      </p>
      <p class="contact__line">
        <svg class="contact__icon" viewBox="0 0 24 24" aria-hidden="true"><path d="M2 5h20v14H2z M2 5l10 8 10-8" /><path d="M2 6l10 7.5L22 6V5H2z" fill="#f7f7f7"/></svg>
        <span>m.feldner@partyvelt.eu</span>
      </p>
      <p class="contact__line">
        <svg class="contact__icon" viewBox="0 0 24 24" aria-hidden="true"><circle cx="12" cy="12" r="10"/><path d="M7 8c2 0 3 1 3 2.5S8.5 13 9 15s2 3 1.5 5M15 4.5c-.5 2 1 3 2.5 3.5s1.5 2.5 0 3.5-1 3 .5 4" stroke="#f7f7f7" stroke-width="2" fill="none"/></svg>
        <span>www.partyvelt.eu</span>
      </p>
    </div>

    <div class="person">
      <p class="person__name">Markus Feldner</p>
      <p class="person__role">Geschaftsfuhrer</p>
    </div>
    <span class="edge-tab"></span>
  </section>

  <section class="card card--back">
    <div class="wordmark"><span class="wordmark__square"></span><span>partyvelt</span></div>
    <p class="back__url">www.partyvelt.eu</p>
  </section>
</body>
</html>
```